Vexaroll needs a newsletter to introduce our new test - Helix Body Balance

I need a newsletter or email design to introduce a new test that my company has to offer called Helix Body Balance. We are launching this genetic test to fitness centers, nutritionists, high end gyms, personal trainers and others. The genetic test looks at 5 genetic markers that are key to how each individual processes nutrients, carbohydrates etc and then provides a comprehensive report for the individual on specific diet plans, exercise regimens and their genetic results. The newsletter should be an exciting announcement of this new test and one that can easily be used via email or via attachments. I have attached some files which provide much more detail. The final design should communicate an opportunity for these potential customers to increase revenue, provide their members with an extraordinary personalized genetic test and to provide a value add to their current offerings.
Updates
Hi,
I forgot to upload a one page marketing piece that i had created as well as the logo for vexaroll. Happy to provide just not sure how to upload them into the project
Target Market(s)
fitness centers, high end gyms, nutritionists, dieticians, personal trainers, health coaches
Colors
Designer to choose colors to be used in the design.
Look and feel
Each slider illustrates characteristics of the customer's brand and the style your logo design should communicate.

```html
<!DOCTYPE html>
<html lang="en">
<head>
<meta charset="utf-8">
<title>Vexaroll – Helix Body Balance Test</title>
<link href="https://fonts.googleapis.com/css2?family=Oswald:wght@400;500;600;700&family=Montserrat:ital,wght@0,400;0,500;0,600;0,700;1,700&display=swap" rel="stylesheet">
<style>
  :root{
    --navy:#0c2440;
    --navy-deep:#071a30;
    --navy-mid:#123a5e;
    --teal:#3ecfc4;
    --teal-soft:#7fded6;
    --teal-pale:#c9f0ec;
    --white:#ffffff;
    --ink:#0d2a45;
  }
  *{box-sizing:border-box;margin:0;padding:0}
  html,body{width:828px;height:1200px;overflow:hidden;background:var(--white)}
  body{font-family:'Montserrat',Arial,sans-serif;color:var(--white)}
  .sheet{position:relative;width:828px;height:1200px;overflow:hidden;background:var(--white)}

  .hero{position:absolute;left:0;top:0;width:828px;height:625px;
    background:radial-gradient(ellipse at 62% 40%, #1e5a86 0%, var(--navy-mid) 35%, var(--navy) 70%, var(--navy-deep) 100%)}
  .hero-art{position:absolute;left:300px;top:40px;width:360px;height:520px;
    background:radial-gradient(ellipse at 50% 50%, rgba(120,200,230,.35) 0%, rgba(30,90,140,.15) 50%, rgba(12,36,64,0) 75%)}
  .hero-left{position:absolute;left:36px;top:50px;width:380px}
  .new{font-family:'Oswald',Arial,sans-serif;font-weight:700;font-size:96px;line-height:1;letter-spacing:1px;color:var(--white)}
  .product{margin-top:14px;font-family:'Oswald',Arial,sans-serif;font-weight:500;font-size:40px;line-height:1.12;color:var(--teal);text-transform:uppercase;letter-spacing:.5px}
  .tagline{margin-top:12px;font-weight:700;font-style:italic;font-size:17px;letter-spacing:.6px;text-transform:uppercase;color:var(--white)}
  .visit{margin-top:30px;font-family:'Oswald',Arial,sans-serif;font-weight:600;font-size:40px;color:var(--teal);letter-spacing:1px}
  .site{font-size:15px;color:var(--white);margin-top:2px}

  .brand{position:absolute;left:500px;top:80px;width:200px;text-align:center}
  .brand-mark{display:block;margin:0 auto 10px;width:46px;height:46px;border-radius:50%;background:var(--teal)}
  .brand-name{font-family:'Montserrat',Arial,sans-serif;font-weight:600;font-size:26px;color:var(--white)}
  .brand-sub{font-size:13px;color:var(--white);margin-top:2px;letter-spacing:.5px}

  .pitch{position:absolute;left:460px;top:405px;width:340px;font-weight:700;font-size:14px;line-height:1.75;letter-spacing:2.5px;text-transform:uppercase;color:var(--white)}
  .discover{position:absolute;left:460px;top:560px;width:300px;height:36px;padding:0 14px;line-height:36px;font-weight:600;font-size:15px;letter-spacing:1px;color:var(--teal);
    background:linear-gradient(90deg, rgba(62,207,196,.25), rgba(62,207,196,0))}

  .photo-active{position:absolute;left:0;top:625px;width:300px;height:300px;
    background:linear-gradient(160deg,#f4f7f9 0%,#dfe8ee 60%,#c7e6e6 100%)}
  .quote{position:absolute;left:300px;top:625px;width:225px;height:300px;background:var(--teal);
    display:flex;align-items:center;justify-content:center;text-align:center;padding:0 26px;
    font-weight:600;font-size:15px;line-height:1.7;letter-spacing:2px;text-transform:uppercase;color:var(--navy)}

  .testing{position:absolute;left:525px;top:620px;width:303px;height:580px;background:var(--navy);padding:36px 26px 0 26px}
  .testing h2{font-family:'Oswald',Arial,sans-serif;font-weight:500;font-size:34px;letter-spacing:2px;color:var(--teal)}
  .testing p{margin-top:16px;font-size:12px;line-height:1.6;color:var(--white)}
  .panel-title{margin-top:30px;font-size:12px;font-weight:600;letter-spacing:.5px;color:var(--teal);text-transform:uppercase}
  .markers{margin-top:12px;border-collapse:collapse;width:100%}
  .markers td{font-size:11.5px;line-height:1.4;padding:3px 0;vertical-align:top;color:var(--white)}
  .markers td.gene{width:62px;font-weight:700;color:var(--teal)}

  .about{position:absolute;left:0;top:925px;width:260px;height:275px;background:var(--teal-pale);padding:38px 24px 0 24px;color:var(--ink)}
  .about h2{font-family:'Oswald',Arial,sans-serif;font-weight:500;font-size:34px;letter-spacing:2px;color:var(--navy)}
  .about p{margin-top:16px;font-size:12px;line-height:1.6}
  .photo-scale{position:absolute;left:260px;top:925px;width:265px;height:275px;
    background:linear-gradient(140deg,#eef3f5 0%,#cfdde3 45%,#7fd3cc 100%)}
</style>
</head>
<body>
<div class="sheet">
  <section class="hero">
    <div class="hero-art" role="img" aria-label="Glowing DNA double helix on a deep blue background"></div>
    <div class="hero-left">
      <div class="new">NEW</div>
      <h1 class="product">Helix Body Balance Test</h1>
      <div class="tagline">Say goodbye to one-size fits all dieting</div>
      <div class="visit">VISIT US AT</div>
      <div class="site">www.vexaroll.com</div>
    </div>
    <div class="brand">
      <span class="brand-mark"></span>
      <div class="brand-name">Vexaroll</div>
      <div class="brand-sub">Rediscover Yourself</div>
    </div>
    <div class="pitch">Let us help your members personalize a diet &amp; exercise ratio that fits them based on their genetic makeup!</div>
    <div class="discover">Discovery starts within</div>
  </section>

  <div class="photo-active" role="img" aria-label="Athletic woman in blue sportswear doing a lunge stretch"></div>
  <div class="quote">A goal without a plan is just a wish</div>

  <section class="testing">
    <h2>TESTING</h2>
    <p>The genetic test looks at 5 genetic markers that are key to how each individual processes nutrients, carbohydrates etc and then provides a comprehensive report for the individual on specific diet plans, exercise regimens and their genetic results.</p>
    <div class="panel-title">The weight management panel includes:</div>
    <table class="markers">
      <tr><td class="gene">FTO</td><td>Appetite regulation and craving frequency</td></tr>
      <tr><td class="gene">MC4R</td><td>Metabolism regulation</td></tr>
      <tr><td class="gene">FABP2</td><td>Dietary fat sources and fat utilization</td></tr>
      <tr><td class="gene">ADRB2</td><td>Carbohydrate digestion and physical activity</td></tr>
      <tr><td class="gene">SHOB1</td><td>Regulation of leptin and insulin</td></tr>
    </table>
  </section>

  <section class="about">
    <h2>ABOUT US</h2>
    <p>Vexaroll is proud to offer a line of genetic tests that allow wellness minded individuals to discover their genetic makeup as it pertains to weight management.</p>
  </section>
  <div class="photo-scale" role="img" aria-label="Bathroom scale with a blue measuring tape"></div>
</div>
</body>
</html>
```